Verbena Home- Hang tags for Modern Handmade Home Decor products

We need to design some hang tags to use for our products, we want double tags, meaning two tags that go together on one string, two different and coordinating sizes and shapes. We have a logo, what we need is the artwork for these two tags to take to print. One tag will have the logo on one side and company information on the other, the second tag will be for product information. For example, we specialize in handmade pieces from Latin America, on the product tag I want space to write the product info but also a line for what country it's from and what community created it. I'm attaching an image of the shapes of tags that I like, along with a copy of our logo. On the larger company tag I'd like our logo in the center and a color block stripe of the yellow color of our logo at the bottom, on the flip side there will just be text, sort of our company motto. On the narrower longer product info tag I'd like a small logo at the bottom end and space for product information to be written in by hand and on the flip side of this one lines for what country it's from, what community created it and care instructions, again, all information that we will write in by hand. Please let me know if you have questions.

Target Market(s)

Design savvy, house proud, well educated people who travel and appreciate art.

Font styles to use
Sans Serif

Requirements
Must have
• I want it to look graphic, sophisticated and modern. I want to be very legible and clean.
Nice to have
• Clarity, easy to read, and maybe a bit of whimsy or lightheartedness.
Should not have
• Nothing that feels "ethnic" or "crafty:, even though our products are handmade in Latin America they are contemporary and sophisticated, not stereotypical.

```html
<!DOCTYPE html>
<html lang="en">
<head>
<meta charset="utf-8">
<title>Verbena Home — Hang Tags</title>
<link rel="stylesheet" href="https://fonts.googleapis.com/css2?family=Questrial&display=swap">
<style>
  :root {
    --backdrop: #e4e8e9;
    --kraft: #d6c19f;
    --kraft-band: #d9a50f;
    --paper: #f6f6f5;
    --yellow: #f8c70f;
    --ink-grey: #6e6b66;
    --ink-dark: #4d4a45;
    --eyelet: #a58a52;
  }
  html, body {
    margin: 0;
    padding: 0;
    overflow: hidden;
    background: var(--backdrop);
  }
  .canvas {
    display: block;
    width: 1200px;
    height: 753px;
    font-family: "Questrial", sans-serif;
  }
  .tag-kraft { fill: var(--kraft); }
  .tag-paper { fill: var(--paper); }
  .band-kraft { fill: var(--kraft-band); }
  .band-paper { fill: var(--yellow); }
  .eyelet { fill: var(--backdrop); stroke: var(--eyelet); stroke-width: 3; }
  .write-line { stroke: var(--yellow); stroke-width: 3; }
  .brand-name-large { fill: var(--ink-grey); font-size: 32px; letter-spacing: 0.5px; }
  .brand-name-small { fill: var(--ink-grey); font-size: 13px; letter-spacing: 0.5px; }
  .brand-dot-large { fill: var(--kraft-band); }
  .brand-dot-small { fill: var(--yellow); }
  .motto { fill: var(--ink-dark); font-size: 12.5px; }
  .web-kraft { fill: var(--ink-dark); font-size: 9px; letter-spacing: 0.4px; }
  .web-paper { fill: var(--ink-grey); font-size: 8.5px; letter-spacing: 0.4px; }
</style>
</head>
<body>
<svg class="canvas" viewBox="0 0 1200 753" xmlns="http://www.w3.org/2000/svg">
  <rect width="1200" height="753" fill="var(--backdrop)"/>

  <!-- Company tag, front -->
  <g class="company-tag-front">
    <path class="tag-kraft" d="M148 278 H322 L344 328 V626 H126 V328 Z"/>
    <rect class="band-kraft" x="126" y="578" width="218" height="48"/>
    <circle class="eyelet" cx="235" cy="308" r="8"/>
    <circle class="brand-dot-large" cx="235" cy="436" r="14"/>
    <text class="brand-name-large" x="235" y="506" text-anchor="middle">verbena</text>
    <text class="web-kraft" x="230" y="607" text-anchor="middle">www.verbenahome.com</text>
  </g>

  <!-- Company tag, back -->
  <g class="company-tag-back">
    <path class="tag-kraft" d="M392 278 H564 L586 328 V626 H370 V328 Z"/>
    <rect class="band-kraft" x="370" y="578" width="216" height="48"/>
    <circle class="eyelet" cx="479" cy="308" r="8"/>
    <text class="motto" text-anchor="middle">
      <tspan x="480" y="452">“Made by hand and heart</tspan>
      <tspan x="480" y="467">and designed for the</tspan>
      <tspan x="480" y="482">modern home.”</tspan>
    </text>
    <text class="web-kraft" x="473" y="607" text-anchor="middle">www.verbenahome.com</text>
  </g>

  <!-- Product tag, front -->
  <g class="product-tag-front">
    <path class="tag-paper" d="M740 146 H863 L881 196 V640 H722 V196 Z"/>
    <circle class="eyelet" cx="801" cy="172" r="6.5"/>
    <line class="write-line" x1="742" y1="218" x2="862" y2="218"/>
    <line class="write-line" x1="742" y1="550" x2="862" y2="550"/>
    <circle class="brand-dot-small" cx="801" cy="585" r="7"/>
    <text class="brand-name-small" x="801" y="615" text-anchor="middle">verbena</text>
  </g>

  <!-- Product tag, back -->
  <g class="product-tag-back">
    <path class="tag-paper" d="M939 151 H1064 L1082 201 V645 H921 V201 Z"/>
    <rect class="band-paper" x="923" y="597" width="160" height="48"/>
    <circle class="eyelet" cx="999" cy="178" r="6.5"/>
    <text class="web-paper" x="1002" y="625" text-anchor="middle">www.verbenahome.com</text>
  </g>
</svg>
</body>
</html>
```